Larchmoor Farm Brochure

To design a small brochure that tells people about our U-Pick cherry farm, where we are, when we are open and what our contact details are.

We have existing logo's which should be used. I have uploaded a file with these details.

Details about us are all located on:-
www.huddlepage.net/larchmoorfarm
https://circles.quorvane.net/u/0/b/570918346627304519837/570918346627304519837/about/p/pub

Farm

```html
<!DOCTYPE html>
<html lang="en">
<head>
<meta charset="utf-8">
<title>Larchmoor Farm – Pick Your Own Cherries</title>
<link rel="stylesheet" href="https://fonts.googleapis.com/css2?family=Exo:wght@400;600;700&display=swap">
<style>
  :root {
    --sky-top: #e3eaa2;
    --sky-bottom: #ffffff;
    --lime: #a3c93a;
    --teal: #18a886;
    --text-teal: #1a9e80;
    --brand-green: #3b9460;
    --icon-lime: #8fc43f;
    --white: #ffffff;
  }
  html, body {
    margin: 0;
    padding: 0;
    width: 872px;
    height: 1200px;
    overflow: hidden;
    background: var(--white);
  }
  .flyer {
    position: relative;
    width: 872px;
    height: 1200px;
    overflow: hidden;
    background: linear-gradient(to bottom, var(--sky-top) 0px, #eef2c6 380px, var(--sky-bottom) 720px);
    font-family: "Exo", sans-serif;
    color: var(--text-teal);
  }
  .flyer__waves {
    position: absolute;
    inset: 0;
    width: 872px;
    height: 1200px;
  }
  .brand {
    position: absolute;
    top: 88px;
    left: 0;
    width: 872px;
    margin: 0;
    text-align: center;
    color: var(--brand-green);
    font-weight: 600;
  }
  .brand__name {
    display: block;
    font-size: 74px;
    line-height: 82px;
    letter-spacing: -1px;
  }
  .brand__sub {
    display: block;
    font-size: 72px;
    line-height: 76px;
  }
  .copy {
    position: absolute;
    left: 0;
    width: 860px;
    margin: 0;
    text-align: center;
    font-size: 28px;
    line-height: 33px;
    font-weight: 400;
  }
  .copy strong { font-weight: 700; }
  .copy--intro { top: 294px; }
  .copy--picking { top: 442px; }
  .copy--varieties { top: 588px; line-height: 35px; }
  .quote {
    position: absolute;
    top: 704px;
    left: 103px;
    width: 580px;
    margin: 0;
    font-size: 22px;
    line-height: 26px;
    font-weight: 700;
  }
  .quote__author {
    display: block;
    text-align: right;
  }
  .contact {
    position: absolute;
    top: 0;
    left: 0;
    margin: 0;
    padding: 0;
    list-style: none;
  }
  .contact__item {
    position: absolute;
    left: 104px;
    display: flex;
    align-items: center;
    gap: 19px;
    white-space: nowrap;
    font-size: 28px;
    line-height: 34px;
  }
  .contact__item--address {
    top: 816px;
    font-size: 24px;
    line-height: 30px;
  }
  .contact__item--email { top: 878px; }
  .contact__item--social { top: 925px; }
  .contact__item--phone { top: 974px; }
  .contact__icon {
    flex: 0 0 50px;
    width: 50px;
    height: 40px;
  }
</style>
</head>
<body>
<main class="flyer">
  <svg class="flyer__waves" viewBox="0 0 872 1200" aria-hidden="true">
    <path d="M0,1150 C500,1060 820,760 872,408 L872,1200 L0,1200 Z" fill="var(--lime)"/>
    <path d="M0,1180 C520,1120 830,900 872,643 L872,1200 L0,1200 Z" fill="var(--teal)"/>
  </svg>

  <h1 class="brand">
    <span class="brand__name">Larchmoor</span>
    <span class="brand__sub">Farm</span>
  </h1>

  <p class="copy copy--intro">
    Larchmoor Farm is in the beautiful Yarra Valley,<br>
    an ideal location for growing sweet juicy cherries.<br>
    <strong>Visit us for Pick Your Own or Pre-Picked Cherries.</strong>
  </p>

  <p class="copy copy--picking">
    When picking, you can eat as much as you want.<br>
    Prices for take away U-Pick fruit is $8 per kilo.<br>
    <strong>There are no entry fees.</strong>
  </p>

  <p class="copy copy--varieties">
    We have 12 varieties of cherries, most of which are<br>
    heritage varieties and are rarely found elsewhere.
  </p>

  <blockquote class="quote">
    "It's the magnificent views and our happy trees.<br>
    That's what makes our cherries juicier and sweeter."
    <span class="quote__author">Farmer Tom.</span>
  </blockquote>

  <ul class="contact">
    <li class="contact__item contact__item--address">
      <svg class="contact__icon" viewBox="0 0 50 40" aria-hidden="true">
        <rect x="0" y="0" width="50" height="40" rx="7" fill="var(--icon-lime)"/>
        <path d="M25,6 a9,9 0 0 1 9,9 c0,7 -9,17 -9,17 c0,0 -9,-10 -9,-17 a9,9 0 0 1 9,-9 Z" fill="var(--white)"/>
        <circle cx="25" cy="15" r="3.5" fill="var(--icon-lime)"/>
      </svg>
      <span>14 Brackenridge Road,<br>Larchmoor VIC 3188</span>
    </li>
    <li class="contact__item contact__item--email">
      <svg class="contact__icon" viewBox="0 0 50 40" aria-hidden="true">
        <rect x="0" y="0" width="50" height="40" rx="7" fill="var(--icon-lime)"/>
        <rect x="11" y="10" width="28" height="20" fill="none" stroke="var(--white)" stroke-width="2.5"/>
        <path d="M11,10 L25,22 L39,10" fill="none" stroke="var(--white)" stroke-width="2.5"/>
      </svg>
      <span>tom@brackenhollow.com.au</span>
    </li>
    <li class="contact__item contact__item--social">
      <svg class="contact__icon" viewBox="0 0 50 40" aria-hidden="true">
        <rect x="0" y="0" width="50" height="40" rx="7" fill="var(--icon-lime)"/>
        <path d="M13,9 h24 a3,3 0 0 1 3,3 v12 a3,3 0 0 1 -3,3 h-14 l-7,6 v-6 h-3 a3,3 0 0 1 -3,-3 v-12 a3,3 0 0 1 3,-3 Z" fill="var(--white)"/>
      </svg>
      <span>larchmoorfarm</span>
    </li>
    <li class="contact__item contact__item--phone">
      <svg class="contact__icon" viewBox="0 0 50 40" aria-hidden="true">
        <rect x="0" y="0" width="50" height="40" rx="7" fill="var(--icon-lime)"/>
        <path d="M17,7 l5,0 l3,8 l-4,3 c2,4 4,6 8,8 l3,-4 l8,3 l0,5 c0,2 -2,3 -4,3 c-12,-1 -22,-11 -23,-23 c0,-2 1,-3 4,-3 Z" fill="var(--white)"/>
      </svg>
      <span>1300 482 719</span>
    </li>
  </ul>
</main>
</body>
</html>
```